Quorbanil Business Cards & Stationery Design
Business Cards & Stationery Design
Quorbanil Business Cards & Stationery Design - Information Technology
Creative Brief
Professional
Neville Prothick
Technical Consultant
47 marbury close fenwick NSW 2012 Australia
nprothick@quorbanil.example
http://www.quorbanil.example
The font used is called Aller, and can be downloaded from : http://www.glyphmerrow.example/buyonline/fonts/aller
www.quorbanil.example

```html
<!DOCTYPE html>
<html lang="en">
<head>
<meta charset="utf-8">
<title>Quorbanil Business Card</title>
<link rel="stylesheet" href="https://fonts.googleapis.com/css2?family=Ubuntu:wght@400;500;700&display=swap">
<style>
  :root {
    --bg: #ecebe8;
    --card: #ffffff;
    --green: #1f8a1f;
    --green-light: #3ba52f;
    --green-dark: #16701a;
    --grey: #4a4a4a;
    --grey-mid: #6b6b6b;
    --charcoal: #2e2e2e;
    --black: #111111;
    --text: #333333;
    --rule: #b9b9b9;
  }
  * { margin: 0; padding: 0; box-sizing: border-box; }
  html, body {
    width: 1200px; height: 901px; overflow: hidden;
    background: var(--bg);
    font-family: "Ubuntu", sans-serif;
  }
  .business-card {
    position: absolute;
    left: 150px; top: 180px;
    width: 900px; height: 540px;
    background: var(--card);
    border-radius: 42px;
    overflow: hidden;
    box-shadow: 0 18px 40px rgba(0,0,0,.18);
  }
  .brand {
    position: absolute;
    left: 60px; top: 120px;
    width: 380px;
    text-align: center;
  }
  .brand-mark {
    width: 78px; height: 78px;
    margin: 0 auto 22px;
    background: var(--green);
  }
  .brand-name {
    font-size: 84px;
    font-weight: 500;
    color: var(--grey);
    letter-spacing: -1px;
    line-height: 1;
  }
  .divider {
    position: absolute;
    left: 478px; top: 40px;
    width: 1px; height: 360px;
    background: var(--rule);
  }
  .contact {
    position: absolute;
    left: 500px; top: 38px;
    color: var(--text);
  }
  .person-name {
    font-size: 26px; font-weight: 700;
    color: var(--green);
  }
  .person-title {
    font-size: 22px; color: var(--grey-mid);
    margin-top: 4px;
  }
  .address {
    font-size: 21px; line-height: 1.3;
    margin-top: 30px;
  }
  .details {
    list-style: none;
    margin-top: 22px;
    font-size: 21px;
    line-height: 1.5;
  }
  .details li {
    display: flex; align-items: center; gap: 12px;
  }
  .icon {
    width: 20px; height: 20px; flex: none;
  }
  .icon-at {
    width: 20px; text-align: center; font-weight: 700; color: var(--grey);
  }
  .footer-band {
    position: absolute;
    left: 0; right: 0; bottom: 0;
    height: 86px;
    display: flex;
  }
  .band-main { flex: 56; background: linear-gradient(180deg, var(--green-light), var(--green)); }
  .band-step1 { flex: 9; background: var(--green-dark); }
  .band-step2 { flex: 9; background: #2f6b2a; }
  .band-step3 { flex: 9; background: var(--grey); }
  .band-step4 { flex: 9; background: var(--charcoal); }
  .band-step5 { flex: 8; background: var(--black); }
</style>
</head>
<body>
  <main class="business-card">
    <section class="brand">
      <div class="brand-mark"></div>
      <div class="brand-name">quorbanil</div>
    </section>

    <div class="divider"></div>

    <section class="contact">
      <h1 class="person-name">Neville Prothick</h1>
      <p class="person-title">Technical Consultant</p>
      <p class="address">47 marbury close<br>fenwick NSW 2012 Australia</p>
      <ul class="details">
        <li><svg class="icon" viewBox="0 0 20 20"><path d="M5 2h3l1 5-2 1.5a10 10 0 0 0 4.5 4.5L13 11l5 1v3c0 1-1 2-2 2C8 17 3 12 3 4c0-1 1-2 2-2z" fill="#4a4a4a"/></svg>1300 555 018</li>
        <li><svg class="icon" viewBox="0 0 20 20"><path d="M5 2h3l1 5-2 1.5a10 10 0 0 0 4.5 4.5L13 11l5 1v3c0 1-1 2-2 2C8 17 3 12 3 4c0-1 1-2 2-2z" fill="#4a4a4a"/></svg>+61 (0) 9 5550 1427</li>
        <li><svg class="icon" viewBox="0 0 20 20"><rect x="5" y="1" width="10" height="18" rx="2" fill="#4a4a4a"/><rect x="7" y="3" width="6" height="11" fill="#fff"/></svg>+61 (0) 455 500 382</li>
        <li><svg class="icon" viewBox="0 0 20 20"><rect x="2" y="7" width="16" height="10" rx="1" fill="#4a4a4a"/><rect x="5" y="2" width="10" height="6" fill="#4a4a4a"/><rect x="5" y="13" width="10" height="2" fill="#fff"/></svg>+61 (0) 9 5550 1428</li>
        <li><span class="icon-at">@</span>nprothick@quorbanil.example</li>
        <li><svg class="icon" viewBox="0 0 20 20"><rect x="2" y="2" width="16" height="16" rx="3" fill="#4a4a4a"/></svg>quorbanil@social</li>
      </ul>
    </section>

    <div class="footer-band">
      <div class="band-main"></div>
      <div class="band-step1"></div>
      <div class="band-step2"></div>
      <div class="band-step3"></div>
      <div class="band-step4"></div>
      <div class="band-step5"></div>
    </div>
  </main>
</body>
</html>
```